Business Card

Need business cards and small flyers for a musical band

Target Market(s)

Promoters, clients seeking to hire a Latin band

Industry/Entity Type

Business

Requirements
Must have
• The name of the band is Orchestra Brisa so want to have the background with a fire design, with black card and the name of the band in RED, maybe a combination of Red with some yellow. See attached idea.
Nice to have
• See attached files for some ideas.

```html
<!DOCTYPE html>
<html lang="en">
<head>
<meta charset="utf-8">
<title>Orchestra Brisa – Business Card</title>
<link rel="stylesheet" href="https://fonts.googleapis.com/css2?family=Baloo+2:wght@600;700;800&display=swap">
<style>
  :root {
    --paper: #ffffff;
    --card-black: #050202;
    --flame-deep: #7a0c04;
    --flame-red: #c8200a;
    --flame-orange: #f06a12;
    --flame-yellow: #ffd23a;
    --name-orange: #f3761c;
    --title-red: #e0301a;
    --contact-yellow: #f4c62a;
    --ink-outline: #1a0602;
    --crop: #000000;
  }
  * { margin: 0; padding: 0; box-sizing: border-box; }
  html, body {
    width: 1200px; height: 731px; overflow: hidden;
    background: var(--paper);
  }
  .sheet { position: relative; width: 1200px; height: 731px; }

  .crop-marks { position: absolute; inset: 0; }

  .card {
    position: absolute; left: 62px; top: 53px;
    width: 1076px; height: 623px;
    background: var(--card-black);
    overflow: hidden;
    font-family: "Baloo 2", "Trebuchet MS", sans-serif;
  }

  .fire-field {
    position: absolute; inset: 0;
    background:
      radial-gradient(ellipse 70% 55% at 40% 100%, rgba(255,210,58,.55), transparent 70%),
      radial-gradient(ellipse 60% 60% at 95% 70%, rgba(240,106,18,.75), transparent 70%),
      radial-gradient(ellipse 90% 60% at 50% 85%, var(--flame-red), transparent 75%),
      radial-gradient(ellipse 110% 50% at 50% 100%, var(--flame-deep), transparent 80%),
      linear-gradient(180deg, var(--card-black) 30%, #2a0603 60%, #6a0e05 100%);
  }

  .clef-flame {
    position: absolute; left: 70px; top: 80px;
    width: 156px; height: 360px;
    border-radius: 50% 50% 45% 45% / 30% 30% 50% 50%;
    background: radial-gradient(ellipse at 50% 55%, var(--flame-yellow) 0%, var(--flame-orange) 40%, rgba(200,32,10,.6) 70%, transparent 85%);
  }

  .band-name {
    position: absolute; left: 0; right: 0; top: 42px;
    text-align: center;
    padding-left: 140px;
    font-size: 178px; font-weight: 800; line-height: 1;
    letter-spacing: 6px;
    color: var(--name-orange);
  }

  .band-word {
    position: absolute; left: 0; right: 0; top: 258px;
    text-align: center; padding-left: 130px;
    font-size: 46px; font-weight: 700; line-height: 1;
    color: var(--title-red);
    text-shadow: -2px -2px 0 var(--ink-outline), 2px -2px 0 var(--ink-outline),
                 -2px 2px 0 var(--ink-outline), 2px 2px 0 var(--ink-outline);
  }

  .contact {
    position: absolute; left: 0; right: 0; top: 360px;
    text-align: center; padding-left: 130px;
    color: var(--contact-yellow);
    text-shadow: -2px -2px 0 var(--ink-outline), 2px -2px 0 var(--ink-outline),
                 -2px 2px 0 var(--ink-outline), 2px 2px 0 var(--ink-outline),
                 3px 3px 0 var(--ink-outline);
    line-height: 1;
  }
  .contact-name { font-size: 42px; font-weight: 700; }
  .contact-role { font-size: 28px; font-weight: 600; margin-top: 4px; }
  .contact-phone { font-size: 38px; font-weight: 700; margin-top: 24px; }
  .contact-email { font-size: 36px; font-weight: 700; margin-top: 10px; }
</style>
</head>
<body>
<div class="sheet">
  <svg class="crop-marks" width="1200" height="731" aria-hidden="true">
    <g stroke="var(--crop)" stroke-width="1.2">
      <line x1="94" y1="0" x2="94" y2="44"/>
      <line x1="1114" y1="0" x2="1114" y2="44"/>
      <line x1="94" y1="687" x2="94" y2="731"/>
      <line x1="1114" y1="687" x2="1114" y2="731"/>
      <line x1="0" y1="80" x2="44" y2="80"/>
      <line x1="1156" y1="80" x2="1200" y2="80"/>
      <line x1="0" y1="648" x2="44" y2="648"/>
      <line x1="1156" y1="648" x2="1200" y2="648"/>
    </g>
  </svg>

  <div class="card">
    <div class="fire-field" role="img" aria-label="Background of swirling red, orange and yellow flames rising across the black card"></div>
    <div class="clef-flame" role="img" aria-label="Treble clef formed of fire"></div>

    <div class="band-name">BRISA</div>
    <div class="band-word">Orchestra</div>

    <div class="contact">
      <div class="contact-name">Rafael Montoya</div>
      <div class="contact-role">Musical Director</div>
      <div class="contact-phone">Cell: 813-555-0142</div>
      <div class="contact-email">e-mail:rafaelm218@brisamail.com</div>
    </div>
  </div>
</div>
</body>
</html>
```